Website re-design for Birchmont LLC website ( has existing website )

Looking to do a complete re-design of Birchmontllc. The existing website is dated and built in wordpress. The new website will not be wordpress. The project folder includes an overview.txt file with details on the project. The file also contains a list of websites that he/she likes which I am sure is very helpful .
Number of Pages Required
1 page

```html
<!DOCTYPE html>
<html lang="en">
<head>
<meta charset="utf-8">
<title>Birchmont LLC</title>
<link href="https://fonts.googleapis.com/css2?family=Montserrat:ital,wght@0,400;0,500;0,600;0,700;1,800&family=Open+Sans:wght@400;600;700&display=swap" rel="stylesheet">
<style>
:root{
  --blue:#0d6ebd;
  --blue-dark:#1a5aa6;
  --ink:#333;
  --body:#555;
  --tile:#e8ebee;
  --page:#f2f2f2;
  --footer:#2b2b2b;
  --white:#fff;
}
*{margin:0;padding:0;box-sizing:border-box}
html,body{width:1200px;height:5093px;overflow:hidden}
body{position:relative;background:var(--page);font-family:"Open Sans",sans-serif;color:var(--body)}
.abs{position:absolute}
.heading{font-family:"Montserrat",sans-serif;font-weight:700;color:var(--ink);text-align:center;letter-spacing:1px}

/* header */
.site-header{position:absolute;left:0;top:0;width:1200px;height:125px;background:var(--white)}
.brand{position:absolute;display:flex;align-items:center;gap:10px}
.brand-mark{width:78px;height:78px;border-radius:50%;background:var(--blue)}
.brand-name{font-family:"Montserrat",sans-serif;font-weight:500;font-size:38px;color:var(--blue);line-height:1}
.brand-tag{font-size:9.5px;font-weight:700;color:#222;margin-top:4px}
.contact-chip{position:absolute;top:34px;display:flex;align-items:center;gap:10px;font-size:12px;color:#333}
.chip-icon{width:26px;height:26px;border-radius:50%;background:#e7eef6;display:flex;align-items:center;justify-content:center}
.chip-label{color:var(--blue);font-size:11px;display:block}
.quote-btn{position:absolute;left:971px;top:30px;width:137px;height:33px;border-radius:17px;background:var(--blue);color:#fff;font-size:12.5px;display:flex;align-items:center;justify-content:center;gap:8px;font-family:"Montserrat",sans-serif}
.quote-btn i{width:16px;height:16px;border-radius:50%;background:#fff;display:inline-block}
.nav{position:absolute;top:82px;font-family:"Montserrat",sans-serif;font-size:13px;letter-spacing:1.2px;color:#333}
.nav.active{color:var(--blue)}
.nav.active::after{content:"";display:block;width:56px;height:2px;background:var(--blue);margin-top:10px;margin-left:-4px}

/* hero */
.hero-photo{position:absolute;left:0;top:125px;width:1200px;height:590px;background:linear-gradient(180deg,#5b7e3e 0%,#4f6e36 45%,#39552b 100%)}
.hero-kicker{position:absolute;top:490px;width:1200px;text-align:center;color:#fff;font-family:"Montserrat",sans-serif;font-size:15px;letter-spacing:.5px}
.hero-title{position:absolute;top:516px;width:1200px;text-align:center;color:#fff;font-family:"Montserrat",sans-serif;font-style:italic;font-weight:800;font-size:29px;line-height:40px;letter-spacing:.5px}
.hero-pager{position:absolute;left:1128px;top:410px;font-size:9px;color:#fff;line-height:18px;text-align:right}

/* about */
.about-ring{position:absolute;left:95px;top:927px;width:506px;height:506px;border-radius:50%;border:5px solid var(--blue);padding:14px;background:var(--page)}
.about-photo{width:100%;height:100%;border-radius:50%;background:linear-gradient(180deg,#c9d3dc 0%,#9aa8b4 55%,#3a3f44 100%)}
.sub-title{position:absolute;font-family:"Montserrat",sans-serif;font-weight:700;font-size:16px;letter-spacing:2px;color:var(--blue)}
.sub-title::after{content:"";display:block;width:40px;height:2px;background:#999;margin-top:6px}
.para{position:absolute;left:652px;width:478px;font-size:13.5px;line-height:26.5px;color:var(--body)}
.btn{position:absolute;background:var(--blue);color:#fff;font-size:13px;display:flex;align-items:center;justify-content:center;border-radius:6px;font-family:"Montserrat",sans-serif}

/* services */
.service-band{position:absolute;left:0;top:1518px;width:1200px;height:612px;background:linear-gradient(180deg,#2c64ad 0%,#1d5aa6 50%,#17539f 100%)}
.service-card{position:absolute;top:1706px;width:242px;height:334px;border-radius:6px;background:#e9edf1;text-align:center;padding-top:34px}
.service-card.is-active{background:var(--blue);color:#fff}
.service-icon{width:100px;height:100px;border-radius:50%;background:var(--blue);margin:0 auto}
.is-active .service-icon{background:#e9edf1}
.card-title{font-family:"Montserrat",sans-serif;font-size:15px;letter-spacing:1.8px;color:#333;margin-top:22px;line-height:19px;height:40px;display:flex;align-items:center;justify-content:center}
.is-active .card-title{color:#fff}
.card-text{font-size:13px;line-height:17px;color:#555;padding:8px 18px 0;height:76px}
.is-active .card-text{color:#fff}
.card-more{font-size:12.5px;color:var(--blue);display:flex;align-items:center;justify-content:center;gap:6px}
.is-active .card-more{color:#fff}
.arrow-dot{width:26px;height:26px;border-radius:50%;background:var(--blue);display:inline-flex;align-items:center;justify-content:center}
.is-active .arrow-dot{background:#fff}

/* testimonials */
.testimonial-band{position:absolute;left:0;top:2130px;width:1200px;height:1187px;background:linear-gradient(180deg,#d9dcdf 0%,#eceef0 25%,#f2f2f2 60%)}
.testimonial-card{position:absolute;top:2303px;width:472px;height:261px;background:linear-gradient(180deg,#3f4446 0%,#55595b 100%);color:#fff;text-align:center;padding:30px 70px 0}
.quote-mark{font-family:"Montserrat",sans-serif;font-weight:700;font-size:74px;line-height:54px;height:58px}
.testimonial-card p{font-size:12.5px;line-height:16px}
.testimonial-card .author{font-weight:700;margin-top:14px}
.dot{position:absolute;top:2612px;width:12px;height:12px;border-radius:50%;background:#3b3b3b}

/* other services */
.other-tile{position:absolute;width:207px;height:208px;border-radius:6px;background:var(--tile);text-align:center;padding-top:34px}
.other-icon{width:76px;height:76px;margin:0 auto;border-radius:14px;background:var(--blue)}
.other-label{font-family:"Montserrat",sans-serif;font-size:16.5px;letter-spacing:1px;color:#333;line-height:21px;margin-top:20px}

/* gallery */
.gallery-band{position:absolute;left:0;top:3317px;width:1200px;height:607px;background:linear-gradient(180deg,#3b6fa9 0%,#2a5f9b 50%,#1e4f88 100%)}

/* faq */
.faq-item{position:absolute;left:597px;width:530px;background:#e6e8ea;border-radius:3px;font-size:13px;color:#444;padding:0 14px;display:flex;align-items:center;justify-content:space-between}
.faq-toggle{width:22px;height:22px;border-radius:50%;background:var(--blue);flex:none;display:flex;align-items:center;justify-content:center}
.page-box{position:absolute;top:4467px;width:34px;height:32px;background:#e3e5e7;font-size:12px;color:#444;display:flex;align-items:center;justify-content:center}
.page-box.current{background:var(--blue);color:#fff}

/* footer */
.footer-col-title{position:absolute;font-family:"Montserrat",sans-serif;font-weight:700;font-size:17px;color:#fff}
.footer-links{position:absolute;left:403px;top:4838px;list-style:none;font-size:13px;color:#fff;line-height:24.5px;letter-spacing:1px}
.footer-links li::before{content:">";margin-right:14px}
.footer-text{position:absolute;font-size:12.5px;color:#fff;line-height:24px}
.social{position:absolute;top:4918px;width:28px;height:28px;border-radius:50%;background:#fff}
.field{position:absolute;background:#fff;border-radius:4px;font-size:12px;color:#888;padding:8px 10px}
.copyright{position:absolute;left:0;top:5021px;width:1200px;height:72px;background:#ececec;font-size:12.5px;color:#444;display:flex;align-items:center;justify-content:center}
.copyright b{color:var(--blue);font-weight:600;margin:0 4px}
</style>
</head>
<body>

<!-- header -->
<header class="site-header">
  <div class="brand" style="left:69px;top:28px">
    <div class="brand-mark"></div>
    <div>
      <div class="brand-name">Birchmont</div>
      <div class="brand-tag">"Caring for your waterfront every season."</div>
    </div>
  </div>
  <div class="contact-chip" style="left:620px">
    <span class="chip-icon"><svg width="12" height="12" viewBox="0 0 24 24"><path fill="#0d6ebd" d="M6.6 10.8a15.1 15.1 0 0 0 6.6 6.6l2.2-2.2c.3-.3.7-.4 1-.2 1.1.4 2.3.6 3.6.6.6 0 1 .4 1 1V20c0 .6-.4 1-1 1A17 17 0 0 1 3 4c0-.6.4-1 1-1h3.5c.6 0 1 .4 1 1 0 1.3.2 2.5.6 3.6.1.3 0 .7-.2 1z"/></svg></span>
    <span><span class="chip-label">Call Us</span>(555) 014-2290</span>
  </div>
  <div class="contact-chip" style="left:780px">
    <span class="chip-icon"><svg width="13" height="10" viewBox="0 0 26 20"><rect x="1" y="1" width="24" height="18" rx="2" fill="#0d6ebd"/><path d="M2 3l11 8 11-8" stroke="#fff" stroke-width="2" fill="none"/></svg></span>
    <span><span class="chip-label">Email us</span>hello@birchmontllc.com</span>
  </div>
  <div class="quote-btn">Get A Quote <i></i></div>
  <nav>
    <span class="nav active" style="left:531px">Home</span>
    <span class="nav" style="left:636px">About Us</span>
    <span class="nav" style="left:766px">Services v</span>
    <span class="nav" style="left:890px">FAQs</span>
    <span class="nav" style="left:990px">Contact Us</span>
    <svg class="abs" style="left:1098px;top:83px" width="14" height="14" viewBox="0 0 14 14"><circle cx="6" cy="6" r="4.5" stroke="#333" stroke-width="1.6" fill="none"/><path d="M9.5 9.5L13 13" stroke="#333" stroke-width="1.6"/></svg>
  </nav>
</header>

<!-- hero -->
<section>
  <div class="hero-photo" role="img" aria-label="Three divers in wetsuits wading through a lake covered in lily pads"></div>
  <div class="hero-kicker">We Know There is No Life Like the Lake Life</div>
  <div class="hero-title">&amp; WE'RE DEDICATED TO KEEPING<br>IT THAT WAY</div>
  <div class="hero-pager">01 —<br>02 •<br>03 •<br>04 •</div>
  <svg class="abs" style="left:0;top:560px" width="1200" height="200" viewBox="0 0 1200 200">
    <path d="M0 75 C220 120 380 190 620 150 C840 115 1000 40 1200 30 L1200 200 L0 200Z" fill="#0d6ebd"/>
    <path d="M0 110 C240 150 380 205 620 175 C860 145 1000 75 1200 70 L1200 200 L0 200Z" fill="#ffffff"/>
    <path d="M0 130 C240 170 380 225 620 195 C860 165 1000 100 1200 95 L1200 200 L0 200Z" fill="#1f7fd0"/>
    <path d="M0 150 C240 185 400 235 640 210 C870 188 1010 125 1200 120 L1200 200 L0 200Z" fill="#f2f2f2"/>
  </svg>
</section>

<!-- about -->
<section>
  <h2 class="heading abs" style="left:0;top:866px;width:1234px;font-size:29px">About Us</h2>
  <div class="about-ring"><div class="about-photo" role="img" aria-label="Young diver in a wetsuit holding a bundle of harvested lake weeds"></div></div>
  <div class="sub-title" style="left:652px;top:959px">Our Mission</div>
  <p class="para" style="top:995px">Birchmont LLC is a company formed in response to the increase in invasive species in Minnesota lakes and waterways. The impact of these fast-growing nuisances inspired our venture to effectively control unwanted lake weeds and create an enjoyable environment craved by waterfront property homeowners.</p>
  <div class="sub-title" style="left:652px;top:1147px">Preserving the Good</div>
  <p class="para" style="top:1183px">We have partnered with Green Loop Compost to recycle 100% of the lake weeds we remove. The types of materials used in compost have a huge impact on how long it takes to break down and how nutrient rich the end product will be. The lake weeds we provide have high levels of moisture as well as critically needed nitrogen. They are a great addition for making high quality compost.</p>
  <div class="btn" style="left:652px;top:1357px;width:135px;height:33px">Read More</div>
</section>

<!-- services -->
<section>
  <div class="service-band" role="img" aria-label="Blue tinted mountain lake landscape"></div>
  <h2 class="heading abs" style="left:0;top:1592px;width:1200px;font-size:28px;color:#fff">Service</h2>
  <p class="abs" style="left:0;top:1637px;width:1210px;text-align:center;color:#fff;font-size:13px;line-height:16px">We know there is no life like the lake life and we are<br>dedicated to keeping it that way.</p>

  <article class="service-card" style="left:73px">
    <div class="service-icon" role="img" aria-label="Diver icon"></div>
    <div class="card-title">Lake Weed Removal<br>(Submerged)</div>
    <p class="card-text">Reclaim open water in front of your dock, beach, or boat slip!</p>
    <div class="card-more">Read More... <span class="arrow-dot"><svg width="8" height="10" viewBox="0 0 8 10"><path d="M2 1l4 4-4 4" stroke="#fff" stroke-width="2" fill="none"/></svg></span></div>
  </article>
  <article class="service-card is-active" style="left:344px">
    <div class="service-icon" role="img" aria-label="Diving mask icon"></div>
    <div class="card-title">Zebra Mussel<br>Removal</div>
    <p class="card-text">This invasive species is becoming an increasing risk to Minnesota waterways...</p>
    <div class="card-more">Read More... <span class="arrow-dot"><svg width="8" height="10" viewBox="0 0 8 10"><path d="M2 1l4 4-4 4" stroke="#0d6ebd" stroke-width="2" fill="none"/></svg></span></div>
  </article>
  <article class="service-card" style="left:616px">
    <div class="service-icon" role="img" aria-label="Seaweed icon"></div>
    <div class="card-title">Shoreline<br>Cleanups</div>
    <p class="card-text">Waves constantly litter trash, lake weeds, and other debris along your shoreline.</p>
    <div class="card-more">Read More... <span class="arrow-dot"><svg width="8" height="10" viewBox="0 0 8 10"><path d="M2 1l4 4-4 4" stroke="#fff" stroke-width="2" fill="none"/></svg></span></div>
  </article>
  <article class="service-card" style="left:886px">
    <div class="service-icon" role="img" aria-label="Sun over waves icon"></div>
    <div class="card-title">Beach Sanding</div>
    <p class="card-text">Continuous waves wash away sand from your beach to expose mud and larger rocks...</p>
    <div class="card-more">Read More... <span class="arrow-dot"><svg width="8" height="10" viewBox="0 0 8 10"><path d="M2 1l4 4-4 4" stroke="#fff" stroke-width="2" fill="none"/></svg></span></div>
  </article>
</section>

<!-- testimonials -->
<section>
  <div class="testimonial-band" role="img" aria-label="Faint misty mountain lake backdrop"></div>
  <h2 class="heading abs" style="left:0;top:2222px;width:1200px;font-size:28px">Testimonials</h2>
  <p class="abs" style="left:0;top:2263px;width:1200px;text-align:center;font-size:12px;color:#555">what client say about us</p>
  <blockquote class="testimonial-card" style="left:113px">
    <div class="quote-mark">“</div>
    <p>Everyone used to jump off the water trampoline and instantly get tangled in lake weeds. We contacted Birchmont and their SCUBA divers have now been solving our problem for the past 4 years!"</p>
    <p class="author">– Pine Hollow Shores Association<br>(Lake Willowmere)</p>
  </blockquote>
  <blockquote class="testimonial-card" style="left:617px">
    <div class="quote-mark">“</div>
    <p>Everyone used to jump off the water trampoline and instantly get tangled in lake weeds. We contacted Birchmont and their SCUBA divers have now been solving our problem for the past 4 years!"</p>
    <p class="author">– Pine Hollow Shores Association<br>(Lake Willowmere)</p>
  </blockquote>
  <span class="dot" style="left:578px;background:var(--blue)"></span>
  <span class="dot" style="left:594px"></span>
  <span class="dot" style="left:610px"></span>
</section>

<!-- other services -->
<section>
  <h2 class="heading abs" style="left:0;top:2680px;width:1176px;font-size:28px">Other Services</h2>
  <div class="other-tile" style="left:109px;top:2752px"><div class="other-icon" role="img" aria-label="Biohazard icon"></div><div class="other-label">Dangerous<br>Object Cleanups</div></div>
  <div class="other-tile" style="left:328px;top:2752px"><div class="other-icon" role="img" aria-label="Sprayer icon"></div><div class="other-label">Emergent Weed<br>Removal</div></div>
  <div class="other-tile" style="left:550px;top:2752px"><div class="other-icon" role="img" aria-label="Floating weed icon"></div><div class="other-label" style="margin-top:26px">Lake Weed Removal<br>(Floating)</div></div>
  <div class="other-tile" style="left:109px;top:2975px"><div class="other-icon" role="img" aria-label="Swimmer icon"></div><div class="other-label">Lost Item<br>Search</div></div>
  <div class="other-tile" style="left:328px;top:2975px"><div class="other-icon" role="img" aria-label="Diver harvesting icon"></div><div class="other-label">Selective<br>Harvesting</div></div>
  <div class="other-tile" style="left:550px;top:2975px"><div class="other-icon" role="img" aria-label="Mask and snorkel icon"></div><div class="other-label">Water Trampoline<br>Management</div></div>
  <div class="abs" style="left:767px;top:2754px;width:316px;height:360px;background:linear-gradient(180deg,#dfe9f3 0%,#6f9ccb 35%,#2f5f98 100%)" role="img" aria-label="Worker on a dock over open lake water"></div>
  <div class="btn" style="left:767px;top:3126px;width:316px;height:57px;font-size:17px;border-radius:4px">View More</div>
</section>

<!-- gallery -->
<section>
  <div class="gallery-band" role="img" aria-label="Deep blue lake with forested hills"></div>
  <h2 class="heading abs" style="left:0;top:3375px;width:1190px;font-size:29px;color:#fff">Our Gallery</h2>
  <div class="abs" style="left:105px;top:3440px;width:986px;height:405px;border:6px solid var(--blue);background:var(--blue)"></div>
  <svg class="abs" style="left:111px;top:3446px" width="974" height="393" viewBox="0 0 974 393">
    <defs>
      <linearGradient id="beforeShade" x1="0" y1="0" x2="0" y2="1"><stop offset="0" stop-color="#b8c7d4"/><stop offset=".4" stop-color="#8a9aa5"/><stop offset="1" stop-color="#6e6640"/></linearGradient>
      <linearGradient id="afterShade" x1="0" y1="0" x2="0" y2="1"><stop offset="0" stop-color="#d3dfeb"/><stop offset=".4" stop-color="#7f98ad"/><stop offset="1" stop-color="#3b5a78"/></linearGradient>
    </defs>
    <polygon points="0,0 500,0 420,393 0,393" fill="url(#beforeShade)" role="img" aria-label="Before: dock area choked with lake weeds"/>
    <polygon points="540,0 974,0 974,393 460,393" fill="url(#afterShade)" role="img" aria-label="After: clear open water by the dock"/>
    <polygon points="480,0 545,0 465,393 420,393" fill="#0d6ebd"/>
  </svg>
  <div class="abs" style="left:565px;top:3530px;color:#fff;font-family:Montserrat,sans-serif;font-weight:700;font-size:17px;transform:rotate(-68deg)">BEFORE</div>
  <div class="abs" style="left:550px;top:3732px;color:#fff;font-family:Montserrat,sans-serif;font-weight:700;font-size:17px;transform:rotate(-68deg)">AFTER</div>
  <div class="abs" style="left:590px;top:3808px;width:495px;height:36px;background:var(--blue);color:#fff;font-family:Montserrat,sans-serif;font-weight:700;font-size:20px;letter-spacing:1.5px;padding:4px 8px">LAKE WEED REMOVAL</div>
  <span class="abs arrow-dot" style="left:96px;top:3620px;width:28px;height:28px;background:#fff"><svg width="8" height="10" viewBox="0 0 8 10"><path d="M6 1L2 5l4 4" stroke="#0d6ebd" stroke-width="2" fill="none"/></svg></span>
  <span class="abs arrow-dot" style="left:1073px;top:3620px;width:28px;height:28px"><svg width="8" height="10" viewBox="0 0 8 10"><path d="M2 1l4 4-4 4" stroke="#fff" stroke-width="2" fill="none"/></svg></span>
</section>

<!-- faqs -->
<section>
  <h2 class="heading abs" style="left:0;top:4013px;width:1206px;font-size:29px">FAQs</h2>
  <div class="abs" style="left:567px;top:4060px;width:80px;height:2px;background:#888"></div>
  <div class="abs" style="left:111px;top:4043px;width:454px;height:454px;border-radius:50%;background:linear-gradient(180deg,#2b6db8 0%,#3a78b8 50%,#1f4d80 100%)" role="img" aria-label="Boat lift frame on a dock over blue water"></div>

  <div class="faq-item" style="top:4092px;height:113px;align-items:flex-start;padding-top:10px">
    <div>
      <div>How early do lake weeds start to grow?</div>
      <p style="font-size:11.5px;line-height:14px;color:#666;margin-top:8px;width:410px">Curly-leaf pondweed is one of the first plants to grow in early spring (and typically dies off the quickest at the end of the summer). This is heavily dependent on sunlight, how fast the water warms up, and sediment type (sand versus muck).</p>
    </div>
    <span class="faq-toggle"><svg width="10" height="8" viewBox="0 0 10 8"><path d="M1 2l4 4 4-4" stroke="#fff" stroke-width="2" fill="none"/></svg></span>
  </div>
  <div class="faq-item" style="top:4223px;height:37px">How fast do lake weeds grow? <span class="faq-toggle"><svg width="8" height="10" viewBox="0 0 8 10"><path d="M6 1L2 5l4 4" stroke="#fff" stroke-width="2" fill="none"/></svg></span></div>
  <div class="faq-item" style="top:4270px;height:37px">How big of an area can I treat? <span class="faq-toggle"><svg width="8" height="10" viewBox="0 0 8 10"><path d="M6 1L2 5l4 4" stroke="#fff" stroke-width="2" fill="none"/></svg></span></div>
  <div class="faq-item" style="top:4316px;height:37px">What if the treatment area encroaches your neighbor's shoreline? <span class="faq-toggle"><svg width="8" height="10" viewBox="0 0 8 10"><path d="M6 1L2 5l4 4" stroke="#fff" stroke-width="2" fill="none"/></svg></span></div>
  <div class="faq-item" style="top:4363px;height:37px">How long does each treatment last? <span class="faq-toggle"><svg width="8" height="10" viewBox="0 0 8 10"><path d="M6 1L2 5l4 4" stroke="#fff" stroke-width="2" fill="none"/></svg></span></div>
  <div class="faq-item" style="top:4409px;height:37px">I DO NOT have a natural beach. Can I install one? <span class="faq-toggle"><svg width="8" height="10" viewBox="0 0 8 10"><path d="M6 1L2 5l4 4" stroke="#fff" stroke-width="2" fill="none"/></svg></span></div>

  <span class="page-box current" style="left:597px">1</span>
  <span class="page-box" style="left:641px">2</span>
  <span class="page-box" style="left:685px">3</span>
  <span class="page-box" style="left:729px">4</span>
  <span class="page-box" style="left:773px">&gt;&gt;</span>
</section>

<!-- footer -->
<footer>
  <svg class="abs" style="left:0;top:4590px" width="1200" height="440" viewBox="0 0 1200 440">
    <path d="M0 20 C200 70 380 120 620 80 C860 40 1000 0 1200 10 L1200 440 L0 440Z" fill="#2b2b2b"/>
  </svg>
  <div class="brand" style="left:81px;top:4784px">
    <div class="brand-mark" style="width:72px;height:72px"></div>
    <div>
      <div class="brand-name" style="font-size:36px">Birchmont</div>
      <div class="brand-tag" style="color:#fff">"Caring for your waterfront every season."</div>
    </div>
  </div>
  <div class="footer-col-title" style="left:185px;top:4883px">Follow us</div>
  <span class="social" style="left:165px"></span>
  <span class="social" style="left:204px"></span>
  <span class="social" style="left:243px"></span>
  <span class="social" style="left:282px"></span>

  <div class="footer-col-title" style="left:403px;top:4778px">Quick Link</div>
  <ul class="footer-links">
    <li>Home</li><li>About Us</li><li>Services</li><li>FAQs</li><li>Contact Us</li>
  </ul>

  <div class="footer-col-title" style="left:552px;top:4776px">Contact info</div>
  <svg class="abs" style="left:547px;top:4841px" width="12" height="16" viewBox="0 0 12 16"><path d="M6 0a6 6 0 0 0-6 6c0 4.5 6 10 6 10s6-5.5 6-10a6 6 0 0 0-6-6z" fill="#fff"/><circle cx="6" cy="6" r="2.2" fill="#2b2b2b"/></svg>
  <div class="footer-text" style="left:577px;top:4836px">1480 Cedar Lane<br>Lindenfield, NW 00412</div>
  <svg class="abs" style="left:546px;top:4908px" width="14" height="11" viewBox="0 0 26 20"><rect x="1" y="1" width="24" height="18" rx="2" fill="#fff"/><path d="M2 3l11 8 11-8" stroke="#2b2b2b" stroke-width="2" fill="none"/></svg>
  <div class="footer-text" style="left:577px;top:4908px">hello@birchmontllc.com<br>(555) 014-2290</div>

  <div class="footer-col-title" style="left:747px;top:4726px">Quick Contact</div>
  <div class="field" style="left:757px;top:4794px;width:115px;height:34px">Name*</div>
  <div class="field" style="left:884px;top:4794px;width:114px;height:34px">Phone*</div>
  <div class="field" style="left:1010px;top:4794px;width:115px;height:34px">Email*</div>
  <div class="field" style="left:757px;top:4840px;width:368px;height:63px">Message</div>
  <div class="btn" style="left:757px;top:4917px;width:115px;height:33px;border-radius:4px;font-size:12px">Submit</div>

  <div class="copyright">Copyright © 2022 <b>BIRCHMONT.</b> All Rights Reserved.</div>
</footer>

</body>
</html>
```